Web Design Project

Current website needs stylish revamping www.plim-ova.com!!!! The look and font should be playful while showing maybe wings, shoes or something that is sexy yet confident for women to wear. The line is a division of a larger company and trademarked under their umbrella entity.

The website should have a clean, trendy and possibly modern look. Important project with hopeful long term business relation ship.

The slogan is also playful...
plim-ova - meant to be seen, not heard
or
plim-ova, light on the feet (hence the idea of wings in the title or website)

plim-ova...., shh, shoes be seen, not heard, light, ect.
Updates

Payment is now guaranteed- we appreciate your work!!!!

Would also like a possible slide show for the home page!!

Not many designs submitted!!! so design away - thank you greatly :)

Kindest regards,
MarnieĀ 

Reason: need a great design for this project- appreciate your help!

Elegant sexy, not trashy!!!

also more clean, sophisticated and modern look- not too busy!!!
clients are high end
thank you so much!!
MarnieĀ 

Target Market(s)

successful, working women

Industry/Entity Type

Business

Requirements
Must have
• Must be clean, buyer and user friendly and embody a sexy feel. Possibly bold colors or mix of neutral beige with black.

```html
<!DOCTYPE html>
<html lang="en">
<head>
<meta charset="utf-8">
<title>plim-ova — meant to be seen, not heard</title>
<link href="https://fonts.googleapis.com/css2?family=Cabin:ital,wght@0,400;0,500;0,600;1,700&family=Lora:ital,wght@1,700&display=swap" rel="stylesheet">
<style>
  :root {
    --paper: #ebebeb;
    --paper-dark: #e2e2e2;
    --charcoal: #333333;
    --ink: #555555;
    --white: #ffffff;
    --accent: #f4453f;
    --ribbon: rgba(232, 82, 70, 0.92);
    --blush: #f7a3a0;
  }
  * { box-sizing: border-box; margin: 0; padding: 0; }
  html, body { width: 1166px; height: 1200px; overflow: hidden; }
  body {
    position: relative;
    background: linear-gradient(var(--paper-dark), var(--paper) 60px) 0 712px / 100% 100% no-repeat, var(--paper);
    font-family: "Cabin", "Gill Sans", sans-serif;
    color: var(--ink);
  }
  .abs { position: absolute; }

  /* Header */
  .header { left: 0; top: 0; width: 1166px; height: 230px; background: var(--paper); border-bottom: 1px solid #bdbdbd; }
  .brand { left: 129px; top: 112px; font-size: 62px; font-weight: 400; color: #1a1a1a; letter-spacing: 1px; line-height: 1; }
  .account { left: 813px; top: 60px; width: 227px; height: 116px; background: var(--charcoal); border-radius: 5px; padding: 12px 13px; }
  .account h2 { font-size: 15px; font-weight: 500; color: var(--white); margin-bottom: 8px; }
  .account .field { height: 23px; background: var(--white); margin-bottom: 6px; padding: 3px 5px; font: italic 700 14px "Cabin", sans-serif; color: #111; }
  .nav { top: 200px; left: 0; width: 1166px; font-size: 18px; font-weight: 600; color: var(--ink); }
  .nav span { position: absolute; white-space: nowrap; }

  /* Feature band */
  .band { left: 0; top: 231px; width: 1166px; height: 481px; background: var(--charcoal); box-shadow: 0 8px 14px rgba(0,0,0,0.12); }
  .side-title { font-family: "Lora", Georgia, serif; font-style: italic; font-weight: 700; color: var(--white); font-size: 26px; }
  .styles { left: 145px; top: 0; list-style: none; color: var(--white); font-size: 18px; }
  .styles li { position: absolute; left: 0; white-space: nowrap; }
  .search-box { left: 139px; top: 582px; width: 189px; height: 32px; background: var(--white); border-radius: 6px; }
  .search-help { left: 142px; top: 618px; font-size: 11px; color: var(--white); white-space: nowrap; }
  .search-help b { font-weight: 600; }
  .search-btn { left: 244px; top: 643px; width: 89px; height: 29px; background: var(--accent); color: var(--white); font-style: italic; font-weight: 700; font-size: 18px; text-align: center; line-height: 28px; }
  .slide { left: 371px; top: 244px; width: 656px; height: 443px; background: linear-gradient(100deg, #8a7a66 0%, #b5916a 35%, #9c5a3c 60%, #d9c7a6 100%); }
  .ribbon { left: 418px; top: 244px; }
  .ribbon-name { left: 418px; top: 268px; width: 193px; text-align: center; color: var(--white); font-family: "Lora", Georgia, serif; font-style: italic; font-weight: 700; font-size: 46px; }
  .ribbon-line { left: 418px; top: 340px; width: 200px; text-align: center; color: var(--white); font-family: "Cabin", sans-serif; font-style: italic; font-weight: 700; font-size: 21px; line-height: 24px; }
  .dots { left: 676px; top: 695px; }

  /* Product grid */
  .tile { width: 215px; height: 174px; background: var(--charcoal); padding: 14px; }
  .shot { width: 100%; height: 100%; background: radial-gradient(ellipse at center, #d9d9d9 0%, #f6f6f6 45%, var(--white) 70%); }
  .shot.red { background: radial-gradient(ellipse at center, #e0342c 0%, #f3a9a5 30%, var(--white) 60%); }
  .shot.black { background: radial-gradient(ellipse at center, #222 0%, #9a9a9a 28%, var(--white) 58%); }
  .shot.tan { background: radial-gradient(ellipse at center, #c9955e 0%, #e8cdb0 30%, var(--white) 60%); }
  .shot.hover { background: radial-gradient(ellipse at center, #c23c38 0%, var(--blush) 40%); position: relative; }
  .quick-view { position: absolute; left: 35px; top: 70px; width: 124px; height: 30px; background: #000; border-radius: 6px; color: var(--white); font-style: italic; font-weight: 700; font-size: 15px; text-align: center; line-height: 30px; }

  /* Footer */
  .footer { left: 0; top: 1134px; width: 1166px; height: 66px; background: var(--charcoal); color: var(--white); font-size: 16px; }
  .footer span { position: absolute; top: 13px; white-space: nowrap; }
</style>
</head>
<body>
  <header class="header abs">
    <div class="brand abs">plim-ova</div>
    <form class="account abs">
      <h2>Sign in or Create an account</h2>
      <div class="field">email</div>
      <div class="field">password</div>
    </form>
    <nav class="nav abs">
      <span style="left:131px">Home</span>
      <span style="left:209px">Collections</span>
      <span style="left:337px">No More Noise</span>
      <span style="left:496px">About Us</span>
      <span style="left:605px">Reviews</span>
      <span style="left:704px">Blog</span>
      <span style="left:776px">Press</span>
      <span style="left:856px">Stores</span>
      <span style="left:939px">Contact Us</span>
    </nav>
  </header>

  <section class="band abs"></section>
  <div class="side-title abs" style="left:137px;top:253px">Choose by style</div>
  <ul class="styles abs">
    <li style="top:311px">Booties</li>
    <li style="top:356px">Flats</li>
    <li style="top:399px">Pumps</li>
    <li style="top:447px">Slingbacks</li>
    <li style="top:495px">View All</li>
  </ul>
  <div class="side-title abs" style="left:151px;top:548px">Search</div>
  <div class="search-box abs"></div>
  <div class="search-help abs"><b>Advanced Search</b> | Search Tips</div>
  <div class="search-btn abs">search</div>

  <div class="slide abs" role="img" aria-label="Woman in a flowing red dress and black heels walking past an ornate railing"></div>
  <svg class="ribbon abs" width="194" height="242" viewBox="0 0 194 242" aria-hidden="true">
    <polygon points="0,0 194,0 194,158 94,240 0,158" fill="var(--ribbon)"/>
  </svg>
  <div class="ribbon-name abs">plim-ova</div>
  <div class="ribbon-line abs">meant to be<br>seen, not heard</div>
  <svg class="dots abs" width="50" height="8" viewBox="0 0 50 8" aria-hidden="true">
    <circle cx="3" cy="4" r="3" fill="#fff"/><circle cx="16" cy="4" r="3" fill="#fff"/>
    <circle cx="29" cy="4" r="3" fill="#fff"/><circle cx="42" cy="4" r="3" fill="#fff"/>
  </svg>

  <main>
    <div class="tile abs" style="left:125px;top:740px"><div class="shot hover" role="img" aria-label="Red peep-toe bootie"><span class="quick-view">quick view</span></div></div>
    <div class="tile abs" style="left:360px;top:740px"><div class="shot black" role="img" aria-label="Black lace-up heeled bootie"></div></div>
    <div class="tile abs" style="left:594px;top:740px"><div class="shot red" role="img" aria-label="Red strappy platform pump"></div></div>
    <div class="tile abs" style="left:828px;top:740px"><div class="shot black" role="img" aria-label="Black patent d'Orsay pump"></div></div>
    <div class="tile abs" style="left:125px;top:929px"><div class="shot black" role="img" aria-label="Black lace-up heeled bootie"></div></div>
    <div class="tile abs" style="left:360px;top:929px"><div class="shot red" role="img" aria-label="Red strappy platform pump"></div></div>
    <div class="tile abs" style="left:594px;top:929px"><div class="shot black" role="img" aria-label="Black patent d'Orsay pump"></div></div>
    <div class="tile abs" style="left:828px;top:929px"><div class="shot tan" role="img" aria-label="Tan buckled peep-toe bootie"></div></div>
  </main>

  <footer class="footer abs">
    <span style="left:289px">My Account</span>
    <span style="left:409px">Order Status</span>
    <span style="left:529px">Wish Lists</span>
    <span style="left:656px">Gift Certificates</span>
    <span style="left:804px">View Cart</span>
  </footer>
</body>
</html>
```